New! Cannabis Infused Chocolates - help us look yummy!

We are a well established cannabis company in Washington State, looking to launch a new line of cannabis infused chocolate squares.

Please see the uploaded inspiration pics - we are hoping to see a collage of the raw ingredients along the side of the front panel of the bag, or possibly as a background texture, but we want to capitalize on the trend of chocolate as "artwork" with the elements that are added to it (toffee or raspberries or nuts etc etc). In this case - raw ingredients illustrations/photos could be chocolate pieces, cocoa beans, leaves or flower of a cocoa plant, toffee pieces/chunks, other decorative elements.

There are a number of "required elements" for state compliance in our state, so I will upload an example of our current 'VOLTA' brand Mint Chocolate packaging so you can see how those "required elements" appear (Not for Kids icon, 21+ icon, the weight, the serving size information, 100mg THC/bag, General Use badge, Nano badge, and all the warning language is the same for this product as the Mint example bag I have uploaded). Please reference the Mint packaging for the icons and copy ONLY - For this contest, we are looking for something drawing from the inspiration pics uploaded.

We are most concerned with the visual concept - so no need to get all the placements, or all of the required elements for this initial contest, we can work together to perfect it once chosen. But in past competitions, designers have found it helpful to know for placement.

***NO CANNABIS IMAGERY PLEASE***

The products are sold in specialty dispensaries so customers are aware the products contain THC. We are more so looking for retail packaging that is trendy, modern, eye catching and enticing for a chocolate food product. The product should look premium and appetizing.

**I have also uploaded several inspiration photos. Design elements such as coco beans, crumbs, flowers, and squares of chocolates are encouraged but please feel free to get creative! We appreciate the designers efforts to put their own twist on the design.

PLEASE NOTE: This is a one bag design - each bag will contain a different flavor but for the purpose of this brief, we are focusing on Toffee Chocolate Bites.

***PLEASE NOTE: For the purpose of this brief, we are focusing on one Chocolate Toffee bag. The winner will have the opportunity to work with us on a 1-1 project to complete the other 5 products in the lineup which are - strawberry, raspberry, peanut butter chip, rice crispy and hemp heart and S'mores*****

Target Market(s)

21+ cannabis chocolate lovers in Washington state

Industry/Entity Type

Cannabis edibles

Requirements
Must have
• Delicious looking renderings of the food - chocolate, toffee, cocoa beans etc
Nice to have
• A collage of the ingredients - the ingredients as artwork - visually appealing and yummy!
Should not have
• NO CANNABIS leaves please. No need to push marijuana imagery.

```html
<!DOCTYPE html>
<html lang="en">
<head>
<meta charset="utf-8">
<title>VOLTA Milk Chocolate Toffee Bites – Pouch Front</title>
<link rel="stylesheet" href="https://fonts.googleapis.com/css2?family=DM+Serif+Display&family=Rokkitt:wght@500;600&family=Barlow+Condensed:wght@600;700;800&display=swap">
<style>
  :root {
    --stage: #d6d7d8;
    --cocoa: #3a2824;
    --forest: #23483a;
    --mint: #1f9a72;
    --cream: #dcd4c6;
    --ink: #2c2220;
    --paper: #f2efeb;
    --warn-red: #d23a33;
    --hazard: #f2e11b;
  }
  * { margin: 0; padding: 0; box-sizing: border-box; }
  html, body { width: 1200px; height: 1200px; overflow: hidden; background: var(--stage); }
  .pouch {
    position: absolute; left: 238px; top: 31px;
    width: 712px; height: 1139px;
    background: var(--cocoa);
    border-radius: 26px;
    overflow: hidden;
  }
  .ingredient-art {
    position: absolute; left: 190px; top: 20px; width: 520px; height: 800px;
    background: radial-gradient(ellipse at 55% 45%, #46322c 0%, #3b2a25 55%, rgba(58,40,36,0) 80%);
  }
  .green-band {
    position: absolute; left: 0; top: 835px; width: 100%; height: 304px;
    background: linear-gradient(180deg, #26503f 0%, var(--forest) 100%);
  }
  .brand-block {
    position: absolute; left: 53px; top: 0; width: 209px; height: 293px;
    background: var(--cream);
    border-bottom: 22px solid var(--mint);
    display: flex; align-items: flex-end; justify-content: center;
    padding-bottom: 26px;
  }
  .brand-name {
    font-family: "DM Serif Display", serif; font-size: 34px; letter-spacing: 1px;
    color: var(--ink);
  }
  .age-badge { position: absolute; left: 459px; top: 73px; width: 108px; height: 108px; }
  .age-badge text {
    font-family: "Barlow Condensed", sans-serif; font-weight: 800; font-size: 17px; fill: var(--ink);
  }
  .kids-badge {
    position: absolute; left: 588px; top: 68px; width: 76px; height: 117px;
    background: var(--paper); border-radius: 2px;
    font-family: "Barlow Condensed", sans-serif; color: var(--warn-red);
  }
  .kids-badge .stop-mark {
    position: absolute; left: 7px; top: 20px; width: 26px; height: 36px;
    background: var(--warn-red); border-radius: 5px;
  }
  .kids-badge .kids-words {
    position: absolute; left: 40px; top: 36px;
    font-size: 11px; font-weight: 800; line-height: 1;
  }
  .kids-badge .emergency {
    position: absolute; left: 0; top: 82px; width: 100%; text-align: center;
    font-size: 10px; font-weight: 700; line-height: 1.2; letter-spacing: 0.3px;
  }
  .strain-pill {
    position: absolute; left: 500px; top: 245px; width: 161px; height: 42px;
    background: var(--mint); border-radius: 10px;
    font-family: "Rokkitt", serif; font-weight: 600; font-size: 34px; letter-spacing: 1px;
    color: var(--ink); text-align: center; line-height: 42px;
  }
  .flavor-line {
    position: absolute; left: 54px; top: 339px;
    font-family: "Rokkitt", serif; font-weight: 600; font-size: 30px; letter-spacing: 0.5px;
    color: var(--paper);
  }
  .product-title {
    position: absolute; left: 48px; top: 395px;
    font-family: "DM Serif Display", serif; font-weight: 400; font-size: 164px; line-height: 1;
    color: var(--paper); letter-spacing: -2px;
  }
  .product-sub {
    position: absolute; left: 60px; top: 584px;
    font-family: "Rokkitt", serif; font-weight: 600; font-size: 64px; letter-spacing: 1px; line-height: 1;
    color: var(--paper);
  }
  .extract-note {
    position: absolute; left: 63px; top: 676px;
    font-family: "Rokkitt", serif; font-weight: 500; font-size: 22px; line-height: 1.15;
    color: var(--paper); text-transform: uppercase;
  }
  .product-render {
    position: absolute; left: 280px; top: 720px; width: 348px; height: 283px;
    background: linear-gradient(180deg, #b98a55 0%, #5a3a2a 30%, #4a2f24 45%, #d9a45a 55%, #c78f45 100%);
    border-radius: 6px;
  }
  .dose-badge {
    position: absolute; left: 72px; top: 869px; width: 80px; height: 69px;
    border: 2px solid var(--mint); border-radius: 8px;
    font-family: "Rokkitt", serif; color: var(--paper); text-align: center;
    padding-top: 6px;
  }
  .dose-badge .amount { display: block; font-size: 17px; font-weight: 500; line-height: 1; }
  .dose-badge .compound { display: block; font-size: 32px; font-weight: 600; line-height: 1; }
  .nano-badge {
    position: absolute; left: 80px; top: 981px; width: 130px;
    font-family: "Barlow Condensed", sans-serif; color: var(--paper);
  }
  .nano-badge .nano-word { font-size: 44px; font-weight: 800; line-height: 0.9; letter-spacing: 0.5px; }
  .nano-badge .nano-dots { position: absolute; left: 92px; top: 6px; }
  .nano-badge .nano-desc { font-size: 12px; font-weight: 800; line-height: 1; text-transform: uppercase; }
  .nano-badge .speed {
    display: inline-block; margin-top: 5px; background: var(--mint);
    padding: 2px 6px; text-align: center;
  }
  .speed .speed-main { display: block; font-size: 20px; font-weight: 800; line-height: 1; }
  .speed .speed-sub { display: block; font-size: 9px; font-weight: 600; letter-spacing: 1px; }
  .net-weight {
    position: absolute; left: 482px; top: 1075px;
    font-family: "Rokkitt", serif; font-weight: 600; font-size: 18px; color: var(--paper);
  }
</style>
</head>
<body>
  <main class="pouch">
    <div class="ingredient-art" role="img" aria-label="Faint line-drawn collage of cocoa pods, cocoa beans, a cocoa flower and chocolate crumbs"></div>
    <div class="green-band"></div>

    <header class="brand-block">
      <span class="brand-name">VOLTA</span>
    </header>

    <svg class="age-badge" viewBox="0 0 108 108" role="img" aria-label="21+ age restriction badge">
      <polygon points="54,2 106,54 54,106 2,54" fill="#ffffff"/>
      <polygon points="54,8 100,54 54,100 8,54" fill="#f2e11b"/>
      <polygon points="14,60 94,60 54,100" fill="#ffffff"/>
      <line x1="14" y1="60" x2="94" y2="60" stroke="#2c2220" stroke-width="1.5"/>
      <text x="54" y="84" text-anchor="middle">21+</text>
    </svg>

    <div class="kids-badge" role="img" aria-label="Not for kids warning badge">
      <span class="stop-mark"></span>
      <span class="kids-words">NOT<br>FOR<br>KIDS</span>
      <span class="emergency">EMERGENCY<br>(800) 555 0142</span>
    </div>

    <div class="strain-pill">SATIVA</div>

    <p class="flavor-line">MILK CHOCOLATE</p>
    <h1 class="product-title">Toffee</h1>
    <p class="product-sub">BITES</p>
    <p class="extract-note">Pure full spectrum<br>Volta distilate</p>

    <div class="product-render" role="img" aria-label="Square of toffee topped with milk chocolate and chopped pecans"></div>

    <div class="dose-badge">
      <span class="amount">100 MG</span>
      <span class="compound">THC</span>
    </div>

    <div class="nano-badge">
      <div class="nano-word">NANO</div>
      <svg class="nano-dots" width="30" height="60" viewBox="0 0 30 60" aria-hidden="true">
        <circle cx="8" cy="10" r="6" fill="none" stroke="#f2efeb" stroke-width="3"/>
        <line x1="12" y1="16" x2="20" y2="44" stroke="#f2efeb" stroke-width="3"/>
        <circle cx="21" cy="50" r="6" fill="none" stroke="#f2efeb" stroke-width="3"/>
      </svg>
      <div class="nano-desc">Emulsified<br>Cannabinoids</div>
      <div class="speed">
        <span class="speed-main">3x FASTER</span>
        <span class="speed-sub">BIOAVAILABILITY</span>
      </div>
    </div>

    <p class="net-weight">Net Wt 2.2 oz. 62g</p>
  </main>
</body>
</html>
```